Personal Injury Lawyer Billboard

I would like a design created featuring the image of the lawyer centered in the middle of the design.
To the left of the lawyer's image it should read "INJURED?"
To the right of the lawyer's image, it should read "CALL DREW!"
Under Call Drew, include the phone number 318-555-0147.
At the bottom of the design include the lawyers information "Andrew Holloway Accident & Injury Lawyers"
PLEASE REMOVED THE BACKGROUND IMAGERY OF THE PHOTO SUBMITTED. Also, the colors for this design should match the colors shown in the logo (navy, white and relective soft gold). Please use those color combinations in ways that best stand out.

```html
<!DOCTYPE html>
<html lang="en">
<head>
<meta charset="utf-8">
<title>Injured? Call Drew! Billboard</title>
<link rel="stylesheet" href="https://fonts.googleapis.com/css2?family=Bebas+Neue&family=Oswald:wght@500&family=Poppins:wght@400&display=swap">
<style>
  :root {
    --backdrop: #0043b3;
    --navy: #0b1b47;
    --navy-glow: #0e3690;
    --gold: #e6bd4b;
    --white: #ffffff;
    --suit-light: #243a82;
    --suit-dark: #13214f;
  }
  * { margin: 0; padding: 0; box-sizing: border-box; }
  html, body {
    width: 1200px;
    height: 600px;
    overflow: hidden;
    background: var(--backdrop);
  }
  .billboard {
    position: absolute;
    left: 37px;
    top: 136px;
    width: 1125px;
    height: 328px;
    overflow: hidden;
    background:
      radial-gradient(ellipse 420px 260px at 560px 250px, var(--navy-glow) 0%, rgba(14,54,144,0) 70%),
      var(--navy);
  }
  .stage {
    position: absolute;
    left: 0; top: 0;
    width: 1125px;
    height: 328px;
  }
  .headline-injured {
    position: absolute;
    left: 38px;
    top: 44px;
    font-family: "Bebas Neue", sans-serif;
    font-weight: 400;
    font-size: 138px;
    line-height: 1;
    letter-spacing: -1px;
    color: var(--gold);
  }
  .firm-mark {
    position: absolute;
    left: 40px;
    top: 170px;
    width: 368px;
    font-family: "Oswald", sans-serif;
    font-weight: 500;
    color: var(--white);
    text-align: center;
  }
  .firm-mark-name {
    display: block;
    font-size: 48px;
    line-height: 60px;
    letter-spacing: -0.5px;
  }
  .firm-mark-tagline {
    display: block;
    margin-top: 9px;
    padding: 4px 0 5px;
    border-top: 2px solid var(--gold);
    border-bottom: 2px solid var(--gold);
    font-size: 29px;
    line-height: 40px;
    letter-spacing: -0.3px;
  }
  .call-to-action {
    position: absolute;
    right: 37px;
    top: 52px;
    text-align: right;
  }
  .cta-headline {
    font-family: "Bebas Neue", sans-serif;
    font-size: 116px;
    line-height: 1;
    color: var(--white);
    letter-spacing: 1px;
  }
  .cta-phone {
    font-family: "Bebas Neue", sans-serif;
    font-size: 74px;
    line-height: 1;
    color: var(--gold);
    margin-top: 2px;
    letter-spacing: 1px;
  }
  .cta-firm {
    font-family: "Poppins", sans-serif;
    font-size: 26px;
    line-height: 35px;
    color: var(--white);
    margin-top: 6px;
  }
</style>
</head>
<body>
  <main class="billboard">
    <svg class="stage" viewBox="0 0 1125 328" aria-hidden="true">
      <defs>
        <linearGradient id="photo-tone" x1="0" y1="0" x2="0" y2="1">
          <stop offset="0" stop-color="var(--suit-light)"/>
          <stop offset="1" stop-color="var(--suit-dark)"/>
        </linearGradient>
      </defs>
      <polygon class="spotlight" points="425,0 694,0 563,215" fill="var(--gold)"/>
    </svg>

    <svg class="stage lawyer-photo" viewBox="0 0 1125 328" role="img" aria-label="Cut-out photo of the lawyer in a navy suit and green tie, smiling with a raised fist">
      <path d="M505,80 Q505,22 560,22 Q615,22 615,80 L615,170 Q660,175 690,200 Q730,230 735,328 L437,328 Q440,240 470,205 Q490,180 505,170 Z"
            fill="url(#photo-tone)" stroke="var(--white)" stroke-width="3"/>
    </svg>

    <h1 class="headline-injured">INJURED?</h1>

    <div class="firm-mark">
      <span class="firm-mark-name">ANDREW HOLLOWAY</span>
      <span class="firm-mark-tagline">ACCIDENT &amp; INJURY LAWYERS</span>
    </div>

    <div class="call-to-action">
      <p class="cta-headline">CALL DREW!</p>
      <p class="cta-phone">318-555-0147</p>
      <p class="cta-firm">Andrew Holloway Accident<br>&amp; Injury Lawyers</p>
    </div>
  </main>
</body>
</html>
```